Business Card + Stationery Design for a Craft Beer Bar

Mr. Tovell's is a taproom sport bar that contains in its menu beers from different places around the world. What we offer differently is the experience that you can get inside our location, ambient music with rock from the 80s to 90s, projection with the sports of the moment, board games and private events.

Target Market(s)

Young people, Mid and High Class

Industry/Entity Type

Business

Font styles to use
Serif
Sans Serif

Colors
fee18a

Requirements
Must have
• Name, Title, Contact Details, Website
Nice to have
• Mail Signature
Should not have
• n/a

```html
<!DOCTYPE html>
<html lang="en">
<head>
<meta charset="utf-8">
<title>Mr. Tovell's – Business Card</title>
<link rel="stylesheet" href="https://fonts.googleapis.com/css2?family=Roboto:wght@300;400;500;700&display=swap">
<style>
  :root {
    --page-bg: #e6e2dc;
    --card-dark: #1c1c1d;
    --card-dark-edge: #2c2c2e;
    --frost-light: #f1efec;
    --frost-mid: #d9d6d2;
    --gold: #e39a2c;
    --gold-soft: #fee18a;
    --text-light: #f2f2f2;
    --text-muted: #d6d6d6;
    --ink: #151515;
  }
  * { margin: 0; padding: 0; box-sizing: border-box; }
  html, body { width: 1200px; height: 970px; overflow: hidden; }
  body {
    background: var(--page-bg);
    font-family: "Roboto", Arial, sans-serif;
  }
  .card {
    position: absolute;
    left: 100px;
    top: 199px;
    width: 1000px;
    height: 572px;
    border-radius: 22px;
    overflow: hidden;
    box-shadow: 0 18px 40px rgba(0,0,0,0.18);
  }
  .card-bg { position: absolute; inset: 0; }
  .contact-name {
    position: absolute; left: 56px; top: 92px;
    font-size: 36px; font-weight: 400; color: var(--text-light); letter-spacing: 0.5px;
  }
  .contact-title {
    position: absolute; left: 57px; top: 131px;
    font-size: 25px; font-weight: 300; color: var(--gold);
  }
  .divider {
    position: absolute; left: 58px; width: 250px; height: 1px;
    background: rgba(255,255,255,0.7);
  }
  .divider.top { top: 191px; }
  .divider.bottom { top: 376px; }
  .contact-list {
    position: absolute; left: 56px; top: 228px; list-style: none;
  }
  .contact-list li {
    display: flex; align-items: center; height: 36px;
    font-size: 25px; font-weight: 300; color: var(--text-muted);
  }
  .contact-list svg { width: 30px; height: 30px; margin-right: 16px; flex: none; }
  .address {
    position: absolute; left: 56px; top: 400px;
    font-size: 25px; font-weight: 300; color: var(--text-muted); line-height: 32px;
  }
  .brand {
    position: absolute; left: 560px; top: 150px; width: 370px;
    display: flex; flex-direction: column; align-items: center;
  }
  .brand-dot {
    width: 70px; height: 70px; border-radius: 50%;
    background: var(--gold);
    margin-bottom: 26px;
  }
  .brand-name {
    font-size: 56px; font-weight: 700; color: var(--ink); letter-spacing: 0.5px;
  }
</style>
</head>
<body>
  <article class="card">
    <svg class="card-bg" viewBox="0 0 1000 572" width="1000" height="572" aria-hidden="true">
      <defs>
        <linearGradient id="frost" x1="0" y1="0" x2="1" y2="1">
          <stop offset="0" stop-color="var(--frost-light)"/>
          <stop offset="1" stop-color="var(--frost-mid)"/>
        </linearGradient>
        <linearGradient id="dark" x1="0" y1="0" x2="1" y2="1">
          <stop offset="0" stop-color="var(--card-dark-edge)"/>
          <stop offset="0.5" stop-color="var(--card-dark)"/>
          <stop offset="1" stop-color="var(--card-dark-edge)"/>
        </linearGradient>
      </defs>
      <rect width="1000" height="572" fill="url(#frost)"/>
      <path class="gold-edge" d="M520 0 C440 150 440 422 520 572" fill="none" stroke="var(--gold)" stroke-width="5" transform="translate(3 0)"/>
      <path class="dark-panel" d="M0 0 H518 C438 150 438 422 518 572 H0 Z" fill="url(#dark)"/>
    </svg>

    <h1 class="contact-name">Owen Hartley</h1>
    <p class="contact-title">Owner</p>
    <div class="divider top"></div>

    <ul class="contact-list">
      <li>
        <svg viewBox="0 0 30 30" aria-hidden="true"><circle cx="15" cy="15" r="13.5" fill="none" stroke="var(--gold)" stroke-width="1.6"/><rect x="10.5" y="7" width="9" height="16" rx="1.5" fill="none" stroke="var(--gold)" stroke-width="1.5"/><line x1="13.5" y1="20.5" x2="16.5" y2="20.5" stroke="var(--gold)" stroke-width="1.4"/></svg>
        (555) 482-1937
      </li>
      <li>
        <svg viewBox="0 0 30 30" aria-hidden="true"><circle cx="15" cy="15" r="13.5" fill="none" stroke="var(--gold)" stroke-width="1.6"/><rect x="8" y="10" width="14" height="10" fill="var(--gold)"/><path d="M8 10 L15 16 L22 10" fill="none" stroke="var(--card-dark)" stroke-width="1.3"/></svg>
        info@tovellstaproom.com
      </li>
      <li>
        <svg viewBox="0 0 30 30" aria-hidden="true"><circle cx="15" cy="15" r="13.5" fill="none" stroke="var(--gold)" stroke-width="1.6"/><circle cx="15" cy="15" r="7.5" fill="none" stroke="var(--gold)" stroke-width="1.3"/><ellipse cx="15" cy="15" rx="3.2" ry="7.5" fill="none" stroke="var(--gold)" stroke-width="1.1"/><line x1="7.5" y1="15" x2="22.5" y2="15" stroke="var(--gold)" stroke-width="1.1"/></svg>
        www.tovellstaproom.com
      </li>
    </ul>

    <div class="divider bottom"></div>
    <p class="address">PO BOX 418 Harbour Lane<br>7th street Northvale</p>

    <div class="brand">
      <div class="brand-dot"></div>
      <p class="brand-name">Mr. Tovell's</p>
    </div>
  </article>
</body>
</html>
```